Gestalten Sie ein tolles Selbstliebe-Buchcover
Design kam bei der Zielgruppe sehr gut an und war professionell umgesetzt. Die Kommunikation läuft zielgerichtet und nett und ich habe schnell alle Dateien bekommen, die ich brauche. Vielen Dank!
Hallo,
schön, dass Sie sich für diese Ausschreibung interessieren. Wir suchen ein Cover für unser Buch, das wir im Selbstverlag veröffentlichen werden.
Titel: Mondgarten am Nordufer
Untertitel 1: Wie du dich von negativen Gedanken befreist und eine liebevolle Beziehung zu dir selbst aufbaust
Untertitel Teil 2: 12 lebensverändernde Monate voller positiver Impulse und Liebe für dich
Das Buch soll (mehrheitlich) Frauen unterstützen, eine liebevolle Beziehung zu sich selbst aufzubauen, negative Gedanken loszulassen und innere Ruhe zu finden.
Aufgabenstellung
Wir sind für jegliche Vorschläge im Rahmen des Themas, der Samples und der Schieberegler offen.
Wichtig ist allerdings
- dass das Design selbst in der kleinen Ansicht (Suchergebnisse) auf Vendora klar hervorsticht, das heißt dort klar erkennbar und die Schrift sofort lesbar ist. Es muss in klein „wirken“, weil viele mit dem Handy auf Vendora shoppen und die Ansicht in den Suchergebnissen dort noch kleiner ist.
- dass das Design die gezielt Emotionen vermittelt
Optimal wäre es, wenn Ihr keine Mockups hochladet. Das macht es viel schwieriger, die Designs einzuschätzen und miteinander zu vergleichen.

```html
<!DOCTYPE html>
<html lang="de">
<head>
<meta charset="utf-8">
<title>Mondgarten am Nordufer – Buchcover</title>
<link rel="stylesheet" href="https://fonts.googleapis.com/css2?family=Courgette&family=Signika:wght@400;500&display=swap">
<style>
  :root {
    --ink: #4a2a36;
    --pink: #e7a3d2;
    --rose: #f0bfe0;
    --lavender: #d9c2e6;
    --cream: #f7e9d6;
    --butter: #f4e3b4;
    --blush: #f3c7d8;
    --page: #ffffff;
  }
  html, body {
    margin: 0;
    padding: 0;
    width: 793px;
    height: 1200px;
    overflow: hidden;
    background: var(--page);
  }
  .cover {
    position: relative;
    width: 793px;
    height: 1200px;
    overflow: hidden;
    color: var(--ink);
  }
  .cover-artwork {
    position: absolute;
    inset: 0;
    background:
      radial-gradient(ellipse 60% 30% at 20% 12%, var(--rose) 0%, transparent 70%),
      radial-gradient(ellipse 50% 25% at 85% 30%, var(--lavender) 0%, transparent 70%),
      radial-gradient(ellipse 55% 22% at 10% 55%, var(--butter) 0%, transparent 70%),
      radial-gradient(ellipse 60% 25% at 80% 85%, var(--blush) 0%, transparent 70%),
      linear-gradient(180deg, var(--pink) 0%, var(--rose) 35%, var(--lavender) 55%, var(--cream) 80%, var(--butter) 100%);
  }
  .cover-title {
    position: absolute;
    left: 120px;
    top: 340px;
    margin: 0;
    font-family: "Courgette", cursive;
    font-weight: 400;
    font-size: 104px;
    line-height: 118px;
    letter-spacing: 0.5px;
  }
  .cover-title span { display: block; }
  .cover-title .line-two { margin-left: -16px; }
  .cover-subtitle {
    position: absolute;
    left: 97px;
    top: 632px;
    width: 620px;
    margin: 0;
    font-family: "Signika", sans-serif;
    font-weight: 500;
    font-size: 29px;
    line-height: 40px;
  }
  .cover-tagline {
    position: absolute;
    left: 97px;
    top: 812px;
    width: 560px;
    margin: 0;
    font-family: "Signika", sans-serif;
    font-weight: 400;
    font-size: 22px;
    line-height: 31px;
  }
</style>
</head>
<body>
  <main class="cover">
    <div class="cover-artwork" role="img" aria-label="Aquarellhintergrund in Rosa, Flieder und Creme mit goldenen und violetten Farbspritzern sowie goldenen Ginkgoblatt-Linien oben links"></div>
    <h1 class="cover-title">
      <span class="line-one">Mondgarten</span>
      <span class="line-two">am Nordufer</span>
    </h1>
    <p class="cover-subtitle">Wie du dich von negativen Gedanken befreist und eine liebevolle Beziehung zu dir selbst aufbaust</p>
    <p class="cover-tagline">12 lebensverändernde Monate voller positiver Impulse und Liebe für dich</p>
  </main>
</body>
</html>
```